Social Media Graphics - Copperfield Loop

Create 6-7 individual social media graphics (square size) to encourage folks to join our online course, using either of the text below (only one set of text per graphic:

The Lantern Ridge Method
How to Create a 7-Figure Business From Scratch
Sign Up Today!

Or

The Lantern Ridge Method
Fast-track Your Way to a Multi-Million Business!
Sign Up Today!

For the color scheme of the graphics, use 1 or 2 colors in the color palette attached; or use any colors that look nice with their outfits; AVOID using red, white and blue altogether because it will look like an Independence Day (4th of July) graphic and we don’t want that; make sure the graphics appeal to both men and women

Make sure each graphic contains 1 of the 2 pics attached; and make sure one of the graphics is all TEXT only.

Target Market(s)

men and women looking to make more money

Industry/Entity Type

entrepreneurship

Requirements
Must have
• see the text document attached
Nice to have
• We are open to a nice color design; the color palette colors are not required, especially we don't want red, white and blue used together
Should not have
• AVOID using red, white and blue altogether because it will look like an Independence Day (4th of July) graphic and we dont want that

```html
<!DOCTYPE html>
<html lang="en">
<head>
<meta charset="utf-8">
<title>The Lantern Ridge Method – Sign Up Today</title>
<link rel="stylesheet" href="https://fonts.googleapis.com/css2?family=Anton&family=Archivo:wdth,wght@125,900&family=Oswald:wght@500&display=swap">
<style>
  :root {
    --brown: #351a0e;
    --green: #1f4520;
    --night: #140b09;
    --gold: #fbb040;
    --photo-warm: #c23a4e;
    --photo-dark: #1c1412;
  }
  * { margin: 0; padding: 0; box-sizing: border-box; }
  html, body { width: 1200px; height: 1200px; overflow: hidden; background: var(--night); }
  .poster {
    position: relative;
    width: 1200px;
    height: 1200px;
    overflow: hidden;
    color: var(--gold);
  }
  .backdrop { position: absolute; inset: 0; }
  .title-tag {
    position: absolute;
    left: 190px; top: 50px;
    width: 820px; height: 102px;
    background: var(--green);
    display: flex; align-items: center; justify-content: center;
    font-family: "Archivo", "Arial Black", sans-serif;
    font-weight: 900;
    font-stretch: 125%;
    font-size: 54px;
    letter-spacing: 2px;
    line-height: 1;
    white-space: nowrap;
  }
  .title-main {
    position: absolute;
    left: 0; right: 0; top: 150px;
    text-align: center;
    font-family: "Anton", "Impact", sans-serif;
    font-size: 232px;
    line-height: 1;
    letter-spacing: 14px;
  }
  .tagline {
    position: absolute;
    left: 62px; top: 420px;
    font-family: "Oswald", "Arial Narrow", sans-serif;
    font-weight: 500;
    font-size: 58px;
    line-height: 117px;
    text-transform: uppercase;
  }
  .hosts-photo {
    position: absolute;
    left: 472px; top: 368px;
    width: 702px; height: 677px;
    background: linear-gradient(90deg, var(--photo-warm) 0%, #a22f40 48%, var(--photo-dark) 55%, #2a211e 100%);
  }
  .cta {
    position: absolute;
    right: 57px; top: 1088px;
    font-family: "Archivo", "Arial Black", sans-serif;
    font-weight: 900;
    font-stretch: 125%;
    font-size: 66px;
    line-height: 1;
    letter-spacing: 1px;
    white-space: nowrap;
  }
</style>
</head>
<body>
  <main class="poster">
    <svg class="backdrop" viewBox="0 0 1200 1200" width="1200" height="1200" aria-hidden="true">
      <defs>
        <linearGradient id="floor-fade" x1="0" y1="0" x2="0" y2="1">
          <stop offset="0" stop-color="#140b09" stop-opacity="0"/>
          <stop offset="1" stop-color="#140b09" stop-opacity="1"/>
        </linearGradient>
      </defs>
      <rect width="1200" height="1200" fill="var(--brown)"/>
      <path d="M795,0 C790,200 720,380 560,560 L161,1056 L1200,1056 V0 Z" fill="var(--green)"/>
      <path d="M410,1045 C420,900 470,780 600,640 C750,480 950,380 1080,410 C1140,425 1180,460 1200,490 V1045 Z" fill="var(--brown)"/>
      <path d="M0,888 L161,1056 L0,1056 Z" fill="var(--night)"/>
      <rect x="0" y="830" width="1200" height="220" fill="url(#floor-fade)"/>
      <rect x="0" y="1045" width="1200" height="155" fill="var(--night)"/>
    </svg>

    <div class="title-tag">THE LANTERN RIDGE</div>
    <h1 class="title-main">METHOD</h1>

    <p class="tagline">Fast-Track<br>Your Way to a<br>Multi-Million<br>Business!</p>

    <div class="hosts-photo" role="img" aria-label="Photo of the two course hosts: a woman in a pink dress with arms crossed and a smiling man in a black jacket"></div>

    <p class="cta">SIGN UP TODAY!</p>
  </main>
</body>
</html>
```